website for 'thebrightnook' which is a specialise tutoring company for children with learning difficu

We need a website for a new business that is focused on assessment and then specialised tutoring for young children with learning difficulties. The website needs to be simple but fun and fresh. We have an existing logo (uploaded) that needs to be the building block for the website. The website doesn't need to be overly content-heavy.

Target Market(s)

parents

Industry/Entity Type

Education

Number of Pages Required

3 page

Font styles to use
Other font styles liked:
• possibly matched to the logo

Requirements
Must have
• a initial front page which introduces the business and provides contact details, a second page that will allow for a more content-heavy section, a third page which focuses on introducing the staff (initially 3 staff ),

```html
<!DOCTYPE html>
<html lang="en">
<head>
<meta charset="utf-8">
<title>The Bright Nook – specialised learning for children</title>
<link rel="stylesheet" href="https://fonts.googleapis.com/css2?family=Montserrat:wght@400;500&family=Noto+Serif:wght@400&family=Open+Sans:ital,wght@0,400;1,400&display=swap">
<style>
:root{
  --green:#8cc63f;
  --yellow:#f0bf00;
  --dark:#3d3b38;
  --ink:#1a1a1a;
  --body:#555;
  --muted:#888;
  --band:#eeeeee;
  --footer:#454545;
  --white:#fff;
}
*{margin:0;padding:0;box-sizing:border-box}
html,body{width:869px;height:1200px;overflow:hidden;background:var(--white)}
body{position:relative;font-family:"Open Sans",sans-serif;color:var(--body)}

.site-header{position:absolute;left:0;top:0;width:869px;height:75px;background:var(--white);z-index:3}
.brand{position:absolute;left:80px;top:-2px;width:204px;height:120px;background:var(--white);border:1px solid #ddd;border-top:none;border-radius:0 0 8px 8px;box-shadow:0 2px 4px rgba(0,0,0,.12);z-index:4;display:flex;flex-direction:column;align-items:center;justify-content:center;padding-top:4px}
.brand-row{display:flex;align-items:center;gap:8px}
.brand-mark{width:16px;height:16px;border-radius:50%;background:var(--green)}
.brand-name{font-family:"Montserrat",sans-serif;font-weight:500;font-size:17px;color:#222;line-height:1}
.brand-tag{font-family:"Open Sans",sans-serif;font-size:9px;color:#666;margin-top:10px}

.main-nav a,.footer-nav a{position:absolute;font-family:"Montserrat",sans-serif;font-size:10.5px;font-weight:500;color:#222;text-decoration:none;white-space:nowrap}
.main-nav a{top:37px}
.main-nav a.active{color:var(--green)}

.hero{position:absolute;left:0;top:75px;width:869px;height:395px;background:#ececec;overflow:hidden}
.hero-photo{position:absolute;left:230px;top:0;width:639px;height:395px;background:linear-gradient(100deg,#e4e0dc 0%,#d9b8a8 22%,#e8dcd4 40%,#8fb3d9 62%,#5d8fc9 80%,#e6e9ec 100%)}
.hero-curve{position:absolute;left:0;top:0;width:869px;height:395px}
.hero-kicker{position:absolute;left:84px;top:145px;font-family:"Noto Serif",serif;font-size:23px;color:var(--green);z-index:2}
.hero-title{position:absolute;left:84px;top:175px;font-family:"Noto Serif",serif;font-size:31px;color:var(--ink);z-index:2}
.slider-dots{position:absolute;left:399px;top:333px;display:flex;gap:3px;z-index:2}
.slider-dots span{width:13px;height:13px;border-radius:50%;background:var(--white)}
.slider-dots span.current{background:transparent;border:2px solid var(--white)}

.welcome-title{position:absolute;left:0;width:869px;top:470px;text-align:center;font-family:"Noto Serif",serif;font-weight:400;font-size:27px;color:var(--ink)}
.welcome-title em{font-style:normal;color:var(--green)}
.welcome-text{position:absolute;left:100px;width:669px;top:511px;text-align:center;font-size:11.3px;line-height:19.3px;color:var(--body)}

.feature{position:absolute;top:603px;width:220px;height:220px;border-radius:50%;border:1px solid;display:flex;align-items:center;justify-content:center}
.feature-disc{width:206px;height:206px;border-radius:50%;display:flex;flex-direction:column;align-items:center;justify-content:center;color:var(--white);text-align:center;padding-top:6px}
.feature-title{font-family:"Montserrat",sans-serif;font-size:15.5px;margin-top:8px}
.feature-text{font-size:9px;line-height:13.5px;margin-top:6px;opacity:.92}
.feature-icon{height:44px}
.f-training{left:89px;border-color:var(--green)}
.f-training .feature-disc{background:linear-gradient(160deg,#9ad84f,#7cc62c)}
.f-grow{left:324px;border-color:#ccc}
.f-grow .feature-disc{background:linear-gradient(160deg,#f4c300,#e9b500)}
.f-start{left:558px;border-color:var(--dark)}
.f-start .feature-disc{background:linear-gradient(160deg,#5a5550,#3a3735)}

.testimonials{position:absolute;left:0;top:862px;width:869px;height:240px;background:var(--band)}
.testimonials h2{position:absolute;left:0;width:869px;top:22px;text-align:center;font-family:"Noto Serif",serif;font-weight:400;font-size:23px;color:#444}
.quote-card{position:absolute;top:68px;width:303px;height:133px;background:var(--white);border-radius:26px 26px 0 26px;padding:20px 24px 0 30px}
.quote-card p{font-style:italic;font-size:10.6px;line-height:18px;color:var(--muted);position:relative}
.quote-card p::before{content:"\201C";position:absolute;left:-10px;top:-4px;font-size:20px;font-style:normal;color:#666;font-family:"Noto Serif",serif}
.quote-card p::after{content:"\201D";font-size:20px;font-style:normal;color:#666;font-family:"Noto Serif",serif;vertical-align:-10px;margin-left:3px;line-height:0}
.quote-card cite{display:block;font-style:normal;font-size:10.5px;color:#444;margin-top:6px;margin-left:-3px}

.site-footer{position:absolute;left:0;top:1102px;width:869px;height:98px;background:var(--footer)}
.footer-nav a{top:30px;color:var(--white)}
.copyright{position:absolute;left:85px;top:54px;font-size:9.5px;color:#bbb}
.social{position:absolute;top:21px;width:27px;height:27px;border-radius:50%;background:#111;display:flex;align-items:center;justify-content:center}
.social span{width:9px;height:9px;border-radius:50%;background:var(--green)}
</style>
</head>
<body>

<header class="site-header">
  <nav class="main-nav">
    <a class="active" href="#" style="left:324px">HOME</a>
    <a href="#" style="left:382px">ABOUT US</a>
    <a href="#" style="left:461px">SERVICES</a>
    <a href="#" style="left:537px">LEARNING</a>
    <a href="#" style="left:616px">TESTIMONIAL</a>
    <a href="#" style="left:710px">CONTACT</a>
  </nav>
</header>

<div class="brand">
  <div class="brand-row">
    <span class="brand-mark"></span>
    <span class="brand-name">The Bright Nook</span>
  </div>
  <div class="brand-tag">specialised learning for children</div>
</div>

<section class="hero">
  <div class="hero-photo" role="img" aria-label="Photo of a smiling tutor helping a young girl write at a table"></div>
  <svg class="hero-curve" viewBox="0 0 869 395" aria-hidden="true">
    <path d="M0 395 C 200 360, 300 357, 434 357 C 600 357, 720 370, 869 392 L869 395 Z" fill="#fff"/>
  </svg>
  <div class="hero-kicker">Training to kids with</div>
  <div class="hero-title">Learning Difficulties</div>
  <div class="slider-dots"><span class="current"></span><span></span><span></span><span></span></div>
</section>

<h1 class="welcome-title">Welcome to The <em>Bright Nook</em></h1>
<p class="welcome-text">interdum nec interdum vel blandit sed nulla In ullamcorper est eget tempor cursus neque mi consectetuer mi a ultricies massa est sed nisl Class aptent taciti sociosqu ad litora torquent per conubia nostra per inceptos hymenaeos Proin nulla arcu nonummy luctus dictum eget fermentum et lorem Nunc porta convallis pede</p>

<div class="feature f-training">
  <div class="feature-disc" role="img" aria-label="Green-toned photo of a teacher working with children">
    <svg class="feature-icon" viewBox="0 0 64 44" fill="none" stroke="#fff" stroke-width="2.2">
      <path d="M32 8 C24 3 12 3 4 6 V38 C12 35 24 35 32 40 C40 35 52 35 60 38 V6 C52 3 40 3 32 8 Z"/>
      <path d="M32 8 V40"/><path d="M9 9 V33 M55 9 V33"/>
    </svg>
    <div class="feature-title">Our Training</div>
    <div class="feature-text">Aorquent per conubia nostra per<br>inceptos hymenaeos Proin</div>
  </div>
</div>

<div class="feature f-grow">
  <div class="feature-disc" role="img" aria-label="Yellow-toned photo of children in a classroom">
    <svg class="feature-icon" viewBox="0 0 64 44" fill="none" stroke="#fff" stroke-width="2.2">
      <path d="M2 14 L32 3 L62 14 L32 25 Z"/>
      <path d="M14 19 V31 C20 38 44 38 50 31 V19"/>
      <path d="M56 16 V30"/>
    </svg>
    <div class="feature-title">How we Grow Kids</div>
    <div class="feature-text">Aorquent per conubia nostra per<br>inceptos hymenaeos Proin</div>
  </div>
</div>

<div class="feature f-start">
  <div class="feature-disc" role="img" aria-label="Dark-toned photo of pupils raising hands in class">
    <svg class="feature-icon" viewBox="0 0 80 44" fill="none" stroke="#fff" stroke-width="4">
      <circle cx="20" cy="24" r="12"/><circle cx="60" cy="24" r="12"/>
      <path d="M32 22 Q40 16 48 22"/><path d="M8 24 H2 M72 24 H78"/>
    </svg>
    <div class="feature-title">Want to Start Now</div>
    <div class="feature-text">Aorquent per conubia nostra per<br>inceptos hymenaeos Proin</div>
  </div>
</div>

<section class="testimonials">
  <h2>Testimonials</h2>
  <blockquote class="quote-card" style="left:125px">
    <p>Curabitur iaculis tempus eros Curabitur vel mi sit amet magna malesuada ultrices Ut nisi erat fermentum vel congue id euismod in elit Fusce ultricies orci ac feugiat suscipit leo massa sodales velit</p>
    <cite>- Mara Delling</cite>
  </blockquote>
  <blockquote class="quote-card" style="left:452px;top:70px">
    <p>Curabitur iaculis tempus eros Curabitur vel mi sit amet magna malesuada ultrices Ut nisi erat fermentum vel congue id euismod in elit Fusce ultricies orci ac feugiat suscipit leo massa sodales velit</p>
    <cite>- Mara Delling</cite>
  </blockquote>
</section>

<footer class="site-footer">
  <nav class="footer-nav">
    <a href="#" style="left:85px">HOME</a>
    <a href="#" style="left:142px">ABOUT US</a>
    <a href="#" style="left:221px">SERVICES</a>
    <a href="#" style="left:297px">LEARNING</a>
    <a href="#" style="left:376px">TESTIMONIAL</a>
    <a href="#" style="left:470px">CONTACT</a>
  </nav>
  <div class="copyright">© 2016 Company Name &nbsp;All right reserved &nbsp;Term of Use</div>
  <a class="social" href="#" aria-label="Social link" style="left:653px"><span></span></a>
  <a class="social" href="#" aria-label="Social link" style="left:687px"><span></span></a>
  <a class="social" href="#" aria-label="Social link" style="left:720px"><span></span></a>
  <a class="social" href="#" aria-label="Social link" style="left:753px"><span></span></a>
</footer>

</body>
</html>
```